Design for Marketing Consulting Agency - Please see attachments

Looking for a very simple site - 3-5 pages, one with a portfolio page to showcase our work where we can leave comments on it. Looking for modern/clean/impactful design to represent our brand. Here is example of what I like: https://www.trelvon.com/en-us/ logo and mood board and copy for website (minus the portfolio). Prefer black/gray/white with pops of color/imagery that come from the logo. Prefer dark hero, more white and pops of the orange and red for the rest of the site.

Target Market(s)

Small to medium size businesses

Font styles to use
Sans Serif

Colors

Designer to choose only greyscale colors for use in the design.

Requirements
Must have
• Please see mood board. Prefer mostly black/white site with pops of color and imagery.
Nice to have
• Sample portfolio page?
Should not have
• Don't make it look 'futuristic' . Try to make it modern and clean.

```html
<!DOCTYPE html>
<html lang="en">
<head>
<meta charset="utf-8">
<title>Brightline Marketing</title>
<link rel="stylesheet" href="https://fonts.googleapis.com/css2?family=Comfortaa:wght@400;700&family=Montserrat:wght@400;500;600;700&display=swap">
<style>
:root{
  --gold:#c8901e;
  --red:#e5402b;
  --dark:#333333;
  --darker:#2b2b2b;
  --slate:#5d6b6b;
  --footer:#5a6565;
  --ink:#2a2a2a;
  --text:#4a4a4a;
  --white:#ffffff;
  --line:#d9d9d9;
}
*{margin:0;padding:0;box-sizing:border-box}
html,body{width:1200px;height:4543px;overflow:hidden}
body{position:relative;font-family:"Montserrat",sans-serif;color:var(--text);background:var(--white)}
.abs{position:absolute}
.display{font-family:"Comfortaa",sans-serif;font-weight:400;color:var(--ink);letter-spacing:.5px}
.btn{position:absolute;display:inline-flex;align-items:center;gap:8px;background:var(--red);color:#fff;font-family:"Comfortaa",sans-serif;font-weight:700;font-size:15px;border-radius:24px;padding:0 30px;height:44px}
.btn .dot{width:14px;height:14px;border-radius:50%;background:#fff;position:relative}
.btn .dot::after{content:"";position:absolute;left:4px;top:4px;border-left:6px solid var(--red);border-top:3px solid transparent;border-bottom:3px solid transparent}
.photo{position:absolute}
p.body{font-size:15.5px;line-height:27px}

/* hero */
.hero{position:absolute;left:0;top:0;width:1200px;height:662px;background:radial-gradient(ellipse at 70% 40%,#2d2c4a 0%,#1a1a2c 50%,#101018 100%)}
.brand{position:absolute;display:flex;align-items:center;gap:14px;font-family:"Montserrat",sans-serif;font-weight:500;color:#fff;font-size:23px;line-height:25px;letter-spacing:.5px}
.brand .sq{width:48px;height:48px;background:var(--gold)}
.nav{position:absolute;left:465px;top:52px;display:flex;gap:44px;font-family:"Comfortaa",sans-serif;font-weight:700;color:#fff;font-size:15px}
.nav-cta{left:970px;top:42px;height:42px}
.hero-copy{position:absolute;left:598px;top:198px;width:560px}
.hero-copy h1{font-family:"Comfortaa",sans-serif;font-weight:700;font-size:38px;line-height:52px;color:#fff;white-space:nowrap}
.hero-copy p{margin-top:18px;width:480px;color:#e8e8ee;font-size:16px;line-height:27px}
.hero-copy .btn{position:relative;margin-top:20px}
.mouse{position:absolute;left:594px;top:578px;width:26px;height:42px;border:2px solid #fff;border-radius:13px}
.mouse::after{content:"";position:absolute;left:10px;top:8px;width:2px;height:8px;background:#fff;border-radius:1px}

/* welcome */
.welcome h2{position:absolute;left:97px;top:770px;font-size:52px;line-height:62px;width:480px}
.who{position:absolute;left:0;top:1327px;width:1200px;height:517px;background:var(--dark)}
.who h2{color:#fff;position:absolute;left:609px;top:115px;font-size:50px}
.who p{position:absolute;left:613px;top:180px;width:490px;color:#e0e0e0}

/* packages */
.section-title{position:absolute;left:0;width:1200px;text-align:center;font-size:52px}
.card{position:absolute;top:1994px;width:311px;height:415px;background:#fff;border-radius:16px;box-shadow:0 4px 18px rgba(0,0,0,.12);padding:28px 24px 0}
.card.featured{background:var(--slate);color:#fff}
.card h3{font-family:"Comfortaa",sans-serif;font-weight:700;font-size:20px;line-height:29px;text-align:center;color:var(--ink)}
.card.featured h3{color:#fff}
.price{font-weight:700;font-size:31px;text-align:center;margin-top:8px;color:var(--ink)}
.card.featured .price{color:#fff}
.meet{font-size:16px;text-align:center;margin-top:8px}
.card ul{list-style:none;margin-top:18px}
.card li{position:relative;padding-left:22px;font-size:16px;line-height:25px;margin-bottom:12px}
.card li::before{content:"";position:absolute;left:0;top:7px;width:12px;height:12px;background:var(--gold)}
.card .btn{left:34px;right:34px;bottom:30px;justify-content:center;height:48px;padding:0 10px}

/* team */
.team{position:absolute;left:0;top:2471px;width:1200px;height:639px;background:#3a3a3a;overflow:hidden}
.team .blob{position:absolute;left:-260px;top:0;width:900px;height:900px;border-radius:50%;background:var(--darker)}
.team h2{position:absolute;left:97px;top:130px;color:#fff;font-size:52px}
.team p{position:absolute;left:97px;top:200px;width:410px;color:#ddd}
.member{position:absolute;width:200px;text-align:center;color:#fff}
.member .ring{width:196px;height:196px;border-radius:50%;border:3px solid var(--gold);padding:8px;margin:0 auto}
.member .ring div{width:100%;height:100%;border-radius:50%;background:linear-gradient(#f1f1f1,#cfcfcf)}
.member b{display:block;font-family:"Comfortaa",sans-serif;font-weight:700;font-size:17px;margin-top:10px}
.member span{font-size:14px}

/* portfolio */
.tile{position:absolute;width:312px;height:199px;box-shadow:0 3px 10px rgba(0,0,0,.15);border:5px solid #fff}

/* contact */
.contact{position:absolute;left:0;top:3742px;width:1200px;height:423px;background:var(--dark)}
.contact h2{position:absolute;left:538px;top:95px;color:#fff;font-size:52px}
.field{position:absolute;border:1px solid #777;background:#3c3c3c;color:#ddd;font-size:15px;padding:8px 14px}

/* footer */
.footer{position:absolute;left:0;top:4165px;width:1200px;height:378px;background:var(--footer);color:#eee}
.footer h4{position:absolute;font-family:"Comfortaa",sans-serif;font-weight:700;font-size:17px;color:#fff}
.footer h4::after{content:"";position:absolute;left:0;top:30px;width:36px;height:2px;background:var(--gold)}
.flinks{position:absolute;left:385px;top:112px;list-style:none;font-size:14.5px}
.flinks li{margin-bottom:34px}
.flinks li::before{content:"›  ";color:var(--red)}
.fcontact{position:absolute;left:567px;top:112px;font-size:14.5px;line-height:24px;width:260px}
.fcontact div{position:relative;padding-left:22px;margin-bottom:10px}
.fcontact svg{position:absolute;left:0;top:5px}
.social{position:absolute;top:225px;width:34px;height:34px;border-radius:50%;background:#fff}
</style>
</head>
<body>

<section class="hero">
  <div class="brand" style="left:97px;top:36px"><span class="sq"></span><span>BRIGHTLINE<br>MARKETING</span></div>
  <nav class="nav"><span>Our Packages</span><span>Our Work</span><span>Our Team</span><span>Contact</span></nav>
  <a class="btn nav-cta">Portfolio <span class="dot"></span></a>
  <div class="photo" role="img" aria-label="Photo of a smiling woman in glasses holding an open laptop" style="left:53px;top:150px;width:530px;height:512px;background:radial-gradient(ellipse at 45% 55%,#efeeee 0%,#d8cfc2 35%,rgba(40,38,60,0) 70%)"></div>
  <div class="hero-copy">
    <h1>We Deliver Simple,<br>Clear, and Impactful<br>Messaging and Designs</h1>
    <p>It's an unfortunate fact – many business owners overthink their marketing. They try to be overly creative or wordy.</p>
    <a class="btn">Discover More <span class="dot"></span></a>
  </div>
  <div class="mouse"></div>
</section>

<section class="welcome">
  <h2 class="display">Welcome to Brightline Marketing</h2>
  <p class="body abs" style="left:99px;top:978px;width:478px">It's an unfortunate fact – many business owners overthink their marketing. They try to be overly creative or wordy, resulting in empty statements, confused consumers, and lost revenue opportunities. Brightline Marketing has a simple, thorough process that we use to understand your customer base and their unique pain points</p>
  <a class="btn" style="left:99px;top:1172px">Read More <span class="dot"></span></a>
  <div class="photo" role="img" aria-label="Photo of a young woman sitting on a bean bag using a laptop" style="left:618px;top:736px;width:482px;height:531px;border-radius:48px;background:linear-gradient(160deg,#eeeeee,#d6d6d6)"></div>
</section>

<section class="who">
  <div class="photo" role="img" aria-label="Photo of a smiling man in a denim shirt working on a laptop" style="left:106px;top:32px;width:476px;height:458px;background:linear-gradient(135deg,#c8901e 0%,#a9b6c4 60%,#333 100%);border-radius:40px 0 0 40px"></div>
  <h2 class="display">Who Are We?</h2>
  <p class="body">Brightline Marketing is a Marketing Agency that delivers a breadth of services from brand/rebrand, strategy, design, and web to digital and print marketing campaigns and trade shows. We bring over 20 years of experience in marketing for both B2B to B2C organizations ranging from 5M to over 200M.</p>
  <a class="btn" style="left:613px;top:378px">Read More <span class="dot"></span></a>
</section>

<h2 class="display section-title" style="top:1905px">Our Packages</h2>
<div class="card" style="left:97px">
  <h3>Website &amp; Messaging Facelift</h3>
  <div class="price">$3000-$4000</div>
  <ul><li>Two homepage mockups.</li><li>One mood board.</li><li>Two versions of value proposition messaging – x words</li></ul>
  <a class="btn">See Case Study <span class="dot"></span></a>
</div>
<div class="card featured" style="left:445px">
  <h3>Simple Brand Rebuild</h3>
  <div class="price">$5000-$6000</div>
  <div class="meet">Meetings necessary: 6-7 hours</div>
  <ul><li>5 logo concepts</li><li>Two homepage mockups</li><li>One brand storyboard Two versions of value proposition messaging</li></ul>
  <a class="btn">See example case study <span class="dot"></span></a>
</div>
<div class="card" style="left:789px">
  <h3>Additional Services Offered</h3>
  <ul><li>Strategic Consulting on Growth Strategies and Building Teams</li><li>Trade Show Management and Booth Designs</li><li>Email Marketing Campaigns</li><li>Digital Marketing Campaigns</li></ul>
  <a class="btn">See Case Study <span class="dot"></span></a>
</div>

<section class="team">
  <div class="blob"></div>
  <h2 class="display">Meet The Team</h2>
  <p class="body">Brightline Marketing is run and managed by Dana Whitcombe. It has a team of experts from content creation to graphic design and digital marketing. Dana is a passionate marketing visionary with 20+ years of experience leading direct and channel marketing teams and creating powerful and effective multi-channel marketing strategies and campaigns.</p>
  <a class="btn" style="left:100px;top:446px">Read More <span class="dot"></span></a>
  <div class="member" style="left:640px;top:70px"><div class="ring"><div role="img" aria-label="Portrait photo of team member Owen Hartley"></div></div><b>Owen Hartley</b><span>Designer</span></div>
  <div class="member" style="left:901px;top:70px"><div class="ring"><div role="img" aria-label="Portrait photo of team member Mira Castell"></div></div><b>Mira Castell</b><span>Designer</span></div>
  <div class="member" style="left:640px;top:352px"><div class="ring"><div role="img" aria-label="Portrait photo of team member Lena Voskuijl"></div></div><b>Lena Voskuijl</b><span>Designer</span></div>
  <div class="member" style="left:901px;top:352px"><div class="ring"><div role="img" aria-label="Portrait photo of team member Jonas Petrak"></div></div><b>Jonas Petrak</b><span>Designer</span></div>
</section>

<h2 class="display section-title" style="top:3165px">Portfolio</h2>
<div class="tile" role="img" aria-label="Portfolio piece: creative agency website mockup" style="left:97px;top:3248px;background:linear-gradient(180deg,#fff 0 12%,#0f1a3a 12% 100%)"></div>
<div class="tile" role="img" aria-label="Portfolio piece: stationery branding mockup" style="left:445px;top:3248px;background:linear-gradient(135deg,#5f6466,#3f4446)"></div>
<div class="tile" role="img" aria-label="Portfolio piece: logo design presentation" style="left:789px;top:3248px;background:#e5402b"></div>
<div class="tile" role="img" aria-label="Portfolio piece: t-shirt mockup" style="left:97px;top:3472px;background:linear-gradient(135deg,#8fae9c,#6f9481)"></div>
<div class="tile" role="img" aria-label="Portfolio piece: coffee packaging design" style="left:445px;top:3472px;background:linear-gradient(135deg,#d9c3a2,#b49a74)"></div>
<div class="tile" role="img" aria-label="Portfolio piece: business card mockup" style="left:789px;top:3472px;background:linear-gradient(135deg,#4a4a4a,#1e1e1e)"></div>

<section class="contact">
  <div class="photo" role="img" aria-label="Photo of a team collaborating around a laptop" style="left:97px;top:40px;width:406px;height:348px;border-radius:44px 44px 44px 0;background:linear-gradient(135deg,#c9b79d,#6d5a48)"></div>
  <h2 class="display">Get In Touch</h2>
  <div class="field" style="left:538px;top:148px;width:276px;height:40px">Name</div>
  <div class="field" style="left:538px;top:198px;width:276px;height:40px">Email</div>
  <div class="field" style="left:538px;top:248px;width:276px;height:40px">Phone</div>
  <div class="field" style="left:824px;top:148px;width:276px;height:140px">Message</div>
  <a class="btn" style="left:540px;top:306px;border-radius:4px;height:42px">Submit <span class="dot"></span></a>
</section>

<footer class="footer">
  <div class="brand" style="left:97px;top:90px"><span class="sq"></span><span>BRIGHTLINE<br>MARKETING</span></div>
  <span class="social" style="left:99px"></span><span class="social" style="left:149px"></span><span class="social" style="left:199px"></span>
  <h4 style="left:385px;top:68px">Quick Links</h4>
  <ul class="flinks"><li>Our Packages</li><li>Our Work</li><li>Our Team</li><li>Contact</li></ul>
  <h4 style="left:567px;top:68px">Contact Us</h4>
  <div class="fcontact">
    <div><svg width="12" height="14" viewBox="0 0 12 14"><path d="M6 0a5 5 0 0 0-5 5c0 4 5 9 5 9s5-5 5-9a5 5 0 0 0-5-5zm0 7a2 2 0 1 1 0-4 2 2 0 0 1 0 4z" fill="#e5402b"/></svg>18 Harbour Lane, Level 3 Northgate, Australia</div>
    <div><svg width="13" height="10" viewBox="0 0 13 10"><rect width="13" height="10" fill="#e5402b"/><path d="M0 0l6.5 5L13 0" stroke="#fff" fill="none"/></svg>hello@brightlinemarketing.com</div>
    <div><svg width="12" height="12" viewBox="0 0 12 12"><path d="M2 0l3 3-1.5 2a8 8 0 0 0 3.5 3.5L9 7l3 3-2 2C4 12 0 8 0 2z" fill="#e5402b"/></svg>02 555 018 274</div>
  </div>
  <h4 style="left:844px;top:68px">Newsletter</h4>
  <div class="abs" style="left:844px;top:122px;width:258px;height:40px;border-radius:20px;background:#eef1f1;color:#888;font-size:14px;padding:11px 18px">Enter email address</div>
  <a class="btn" style="left:844px;top:172px;width:258px;justify-content:center;height:40px">Subscribe <span class="dot"></span></a>
  <div class="abs" style="left:97px;top:323px;width:1006px;height:1px;background:#8a9494"></div>
  <div class="abs" style="left:0;top:340px;width:1200px;text-align:center;font-size:14px">© 2022 <span style="color:var(--gold)">Brightline Marketing.</span> All right reserved</div>
</footer>

</body>
</html>
```